Rising Paths Web Design

I am starting a new company that will provide LIFE COACHING services - I have tried to design a website, but it's too complicated. Right now, it's just me - I'm the only person that will provide services through the website - I have used artmarket to purchase a logo (see below). I want to be able to update the website myself, but need a template - basic design. Because I am not technologically savvy enough to explain in words - I basically want to have a website that will provide basic information about my services (coaching), a page about me and my background, hopefully scheduling possibilities, and testimonials — also a page for writing/blogs. I bought a website through NetHarbor - so when I have a template, I guess I”d use that - but maybe I’ll need to work with a designer to actually get it up on the internet. I have a head shot that I’ll upload, too.
Target Market(s)
Clients from the independent (private school) world - teachers, administrators
Number of Pages Required
4 page
Look and feel
Each slider illustrates characteristics of the customer's brand and the style your logo design should communicate.

```html
<!DOCTYPE html>
<html lang="en">
<head>
<meta charset="utf-8">
<title>Rising Paths Coaching</title>
<link rel="stylesheet" href="https://fonts.googleapis.com/css2?family=Questrial&family=Poppins:wght@400;500;600&family=Marck+Script&display=swap">
<style>
:root{
  --teal:#0d9a90;
  --teal-dark:#0a7f76;
  --teal-deep:#07645d;
  --ink:#222;
  --muted:#555;
  --navy:#2d2a6e;
  --footer:#1c1f27;
  --footer-line:#2c303a;
  --footer-text:#a7abb3;
  --topbar:#25272c;
  --blue:#3b82e6;
  --card-bg:#eeeeee;
  --white:#fff;
}
*{box-sizing:border-box;margin:0;padding:0}
html,body{width:683px;height:1200px;overflow:hidden;background:var(--white)}
body{position:relative;font-family:"Questrial",sans-serif;color:var(--ink)}
.abs{position:absolute}

/* header */
.header{left:0;top:0;width:683px;height:77px;background:var(--white)}
.brand{left:80px;top:5px;width:66px;height:66px;border:1.5px solid var(--teal);border-radius:50%}
.brand-name{left:70px;top:32px;width:100px;text-align:center;font-size:9.5px;color:#333;letter-spacing:.2px}
.brand-sub{left:70px;top:45px;width:100px;text-align:center;font-size:4.5px;color:var(--teal);letter-spacing:1px}
.topbar{left:475px;top:0;width:208px;height:14px;background:var(--topbar);clip-path:polygon(10px 0,100% 0,100% 100%,0 100%)}
.topbar-dot{top:4px;width:6px;height:6px;border-radius:50%;background:var(--white)}
.tagline{left:413px;top:26px;font-family:"Marck Script",cursive;font-size:15px;color:var(--teal-dark)}
.nav{left:220px;top:52px;width:463px;height:25px;background:var(--teal);clip-path:polygon(18px 0,100% 0,100% 100%,0 100%)}
.nav-active{left:220px;top:52px;width:72px;height:25px;background:var(--teal-deep);clip-path:polygon(18px 0,100% 0,82% 100%,0 100%)}
.nav-link{top:61px;font-size:7.5px;color:var(--white);letter-spacing:.2px}
.cta{left:525px;top:56px;width:76px;height:17px;background:var(--white);color:var(--teal-dark);font-family:"Poppins",sans-serif;font-weight:600;font-size:6px;text-align:center;line-height:17px}

/* hero */
.hero{left:0;top:77px;width:683px;height:251px;background:linear-gradient(100deg,#6b7f5e 0%,#8d9a7a 30%,#4f7a45 55%,#a9b99a 80%,#6e8f5b 100%)}
.hero-band{left:0;top:328px;width:683px;height:4px;background:var(--teal)}
.hero-title{left:79px;top:145px;font-size:26px;color:var(--white);letter-spacing:.5px}
.hero-text{left:80px;top:185px;width:230px;font-size:8.3px;line-height:13px;color:var(--white)}
.hero-btn{left:79px;top:242px;width:76px;height:22px;background:var(--teal);color:var(--white);font-size:8px;text-align:center;line-height:22px;font-family:"Poppins",sans-serif;font-weight:500}
.slide-nav{left:36px;top:158px;width:12px;font-size:6px;color:var(--white);text-align:center;line-height:12px}
.slide-nav .arrow{color:var(--teal);font-size:9px}

/* story */
.story-title{left:79px;top:370px;font-size:19px;color:var(--teal-dark);letter-spacing:.3px}
.story-text{left:79px;top:409px;width:275px;font-size:7.6px;line-height:12.7px;color:var(--ink)}
.read-more{left:79px;top:498px;font-size:6.5px;color:var(--ink);text-decoration:underline}
.portrait{left:437px;top:366px;width:166px;height:166px;border-radius:50%;background:radial-gradient(circle at 50% 45%,#d9c9a8 0%,#b9a78c 45%,#7d7468 100%)}
.story-rule{left:0;top:558px;width:683px;height:4px;border-top:1px solid var(--teal);border-bottom:1px solid var(--teal)}

/* blog */
.blog-title{left:0;top:588px;width:683px;text-align:center;font-size:16px;color:var(--teal-dark);letter-spacing:.3px}
.post{top:626px;width:165px;height:243px;background:var(--card-bg);border-radius:3px}
.post-img{top:626px;width:165px;height:130px;border-radius:3px 3px 0 0}
.post-body{top:738px;width:145px;height:119px;background:var(--white);box-shadow:0 1px 3px rgba(0,0,0,.12)}
.post-date{top:722px;width:28px;height:28px;border-radius:50%;color:var(--white);font-family:"Poppins",sans-serif;font-size:6px;line-height:7px;text-align:center;padding-top:7px;border:2px solid var(--white)}
.post-meta{font-family:"Poppins",sans-serif;font-size:5.5px;color:#888;top:752px}
.post-title{top:765px;font-family:"Poppins",sans-serif;font-size:9.5px;color:var(--ink)}
.post-title.featured{color:var(--navy)}
.post-text{top:786px;width:125px;font-family:"Poppins",sans-serif;font-size:6px;line-height:12.5px;color:var(--muted)}
.post-more{top:834px;font-family:"Poppins",sans-serif;font-size:6px;font-weight:600;color:var(--ink)}
.post-more.featured{color:var(--teal)}

/* footer */
.footer{left:0;top:899px;width:683px;height:259px;background:var(--footer)}
.f-brand{left:89px;top:921px;width:66px;height:66px;border:1.5px solid var(--teal);border-radius:50%}
.f-brand-name{left:72px;top:949px;width:100px;text-align:center;font-size:9px;color:var(--white)}
.f-brand-sub{left:72px;top:962px;width:100px;text-align:center;font-size:4.5px;color:var(--teal);letter-spacing:1px}
.f-text{left:81px;top:1004px;width:125px;font-size:7.3px;line-height:12.7px;color:var(--footer-text)}
.f-contact{left:81px;font-size:7px;color:var(--footer-text)}
.f-contact svg{vertical-align:-1px;margin-right:8px}
.f-head{top:951px;font-family:"Poppins",sans-serif;font-weight:600;font-size:7.5px;color:var(--white);letter-spacing:.3px}
.f-link{left:215px;font-size:7px;color:var(--footer-text)}
.f-link::before{content:"";display:inline-block;border-left:3px solid var(--footer-text);border-top:2px solid transparent;border-bottom:2px solid transparent;margin-right:6px;vertical-align:1px}
.f-link.current{color:var(--white)}
.tile{width:38px;height:34px;background:var(--white)}
.tile.active{background:var(--blue)}
.sub-label{left:481px;top:1005px;font-size:6.5px;color:var(--footer-text)}
.sub-input{left:481px;top:1022px;width:120px;height:19px;background:#2a2e38;font-size:6.5px;color:var(--footer-text);line-height:19px;padding-left:9px}
.sub-send{left:586px;top:1027px}
.sub-rule{left:481px;top:1058px;width:120px;height:1px;background:var(--footer-line)}
.social{top:1074px;width:18px;height:18px;border-radius:50%;background:#2e323c}
.social.active{background:var(--blue)}
.social::after{content:"";position:absolute;left:7px;top:7px;width:4px;height:4px;border-radius:50%;background:var(--white)}
.copyright{left:0;top:1158px;width:683px;height:42px;background:var(--teal-dark);color:var(--white);font-size:7px;text-align:center;line-height:42px}
</style>
</head>
<body>

<!-- header -->
<div class="abs header"></div>
<div class="abs brand"></div>
<div class="abs brand-name">RISING PATHS</div>
<div class="abs brand-sub">COACHING</div>
<div class="abs topbar"></div>
<span class="abs topbar-dot" style="left:489px"></span>
<span class="abs topbar-dot" style="left:514px"></span>
<span class="abs topbar-dot" style="left:539px"></span>
<span class="abs topbar-dot" style="left:565px"></span>
<span class="abs topbar-dot" style="left:591px"></span>
<div class="abs tagline">Life Is One Time - Make It Memorable</div>
<nav>
  <div class="abs nav"></div>
  <div class="abs nav-active"></div>
  <span class="abs nav-link" style="left:249px;font-weight:600">HOME</span>
  <span class="abs nav-link" style="left:292px">ABOUT US</span>
  <span class="abs nav-link" style="left:345px">OUR MISSION</span>
  <span class="abs nav-link" style="left:410px">CONTACT</span>
  <div class="abs cta">GET APPOINTMENT</div>
</nav>

<!-- hero -->
<div class="abs hero" role="img" aria-label="Photo of a woman in a green jacket stretching on a park path"></div>
<div class="abs hero-band"></div>
<div class="abs slide-nav"><div class="arrow">↑</div><div>01.</div><div>02.</div><div>03.</div><div>04.</div><div class="arrow">↓</div></div>
<h1 class="abs hero-title" style="font-weight:400">JOIN US</h1>
<p class="abs hero-text">Lorem Ipsum is simply dummy text of the printing and typesetting industry. Lorem Ipsum has been the industry's standard dummy text ever since the 1500s.</p>
<div class="abs hero-btn">JOIN</div>

<!-- story -->
<h2 class="abs story-title" style="font-weight:400">SOME STORY BEHIND US</h2>
<p class="abs story-text">Contrary to popular belief, Lorem Ipsum is not simply random text. It has roots in a piece of classical Latin literature from 45 BC, making it over 2000 years old. Elias Norwood, a Latin professor at Westbrook College in Virginia, looked up one of the more obscure Latin words, consectetur, from a Lorem Ipsum passage, and going through the cites of the word in classical literature, discovered the undoubtable source.</p>
<div class="abs read-more">READ MORE</div>
<svg class="abs" style="left:420px;top:350px" width="200" height="200" viewBox="0 0 200 200" aria-hidden="true">
  <circle cx="100" cy="100" r="94" fill="none" stroke="var(--teal)" stroke-width="1.4"/>
  <circle cx="101" cy="101" r="90" fill="none" stroke="var(--teal)" stroke-width="0.8"/>
</svg>
<div class="abs portrait" role="img" aria-label="Head-shot portrait of the coach"></div>
<div class="abs story-rule"></div>

<!-- blog -->
<h2 class="abs blog-title" style="font-weight:400">LATEST BLOG FEEDS</h2>

<article>
  <div class="abs post" style="left:81px"></div>
  <div class="abs post-img" style="left:81px;background:linear-gradient(160deg,#9cc2d8 0%,#c9d9b0 50%,#6f9f55 100%)" role="img" aria-label="Group joining hands outdoors"></div>
  <div class="abs post-body" style="left:91px"></div>
  <div class="abs post-date" style="left:196px;background:var(--teal)">25<br>July</div>
  <span class="abs post-meta" style="left:107px">● Rowan &nbsp;&nbsp;&nbsp;&nbsp;&nbsp; ▪ Cardiology</span>
  <h3 class="abs post-title featured" style="left:106px;font-weight:400">Donec venenatis turpis</h3>
  <p class="abs post-text" style="left:107px">We are an inventive organization thay We've won a huge amount of grants and have been thay highlighted.</p>
  <span class="abs post-more featured" style="left:107px">Reading...</span>
</article>

<article>
  <div class="abs post" style="left:259px"></div>
  <div class="abs post-img" style="left:259px;background:linear-gradient(170deg,#7fae5a 0%,#a7c483 45%,#d7d0b8 100%)" role="img" aria-label="People exercising in a park"></div>
  <div class="abs post-body" style="left:269px"></div>
  <div class="abs post-date" style="left:374px;background:#666">25<br>July</div>
  <span class="abs post-meta" style="left:285px">● Rowan &nbsp;&nbsp;&nbsp;&nbsp;&nbsp; ▪ Cardiology</span>
  <h3 class="abs post-title" style="left:284px;font-weight:400">Donec venenatis turpis</h3>
  <p class="abs post-text" style="left:285px">We are an inventive organization thay We've won a huge amount of grants and have been thay highlighted.</p>
  <span class="abs post-more" style="left:285px">Reading...</span>
</article>

<article>
  <div class="abs post" style="left:437px"></div>
  <div class="abs post-img" style="left:437px;background:linear-gradient(160deg,#5e8f3a 0%,#9cc65a 50%,#c8d86a 80%,#e3a340 100%)" role="img" aria-label="Fresh fruit and vegetables"></div>
  <div class="abs post-body" style="left:447px"></div>
  <div class="abs post-date" style="left:552px;background:#666">25<br>July</div>
  <span class="abs post-meta" style="left:463px">● Rowan &nbsp;&nbsp;&nbsp;&nbsp;&nbsp; ▪ Cardiology</span>
  <h3 class="abs post-title" style="left:462px;font-weight:400">Donec venenatis turpis</h3>
  <p class="abs post-text" style="left:463px">We are an inventive organization thay We've won a huge amount of grants and have been thay highlighted.</p>
  <span class="abs post-more" style="left:463px">Reading...</span>
</article>

<!-- footer -->
<footer>
  <div class="abs footer"></div>
  <div class="abs f-brand"></div>
  <div class="abs f-brand-name">RISING PATHS</div>
  <div class="abs f-brand-sub">COACHING</div>
  <p class="abs f-text">Lorem Ipsum is simply dummy text of the printing and typesetting industry. Lorem Ipsum is simply dummy text of the printing.</p>
  <div class="abs f-contact" style="top:1066px"><svg width="7" height="7" viewBox="0 0 10 10"><rect width="10" height="10" rx="1.5" fill="var(--footer-text)"/><path d="M3 2.5 4.2 4 3.6 4.8C4.2 5.8 4.9 6.5 5.6 6.9L6.3 6.2 7.8 7.3 7.2 8.3C4.7 8 2.4 5.6 2 3.2Z" fill="var(--footer)"/></svg>+1200-555-0148</div>
  <div class="abs f-contact" style="top:1081px"><svg width="7" height="7" viewBox="0 0 10 10"><rect width="10" height="10" rx="1.5" fill="var(--footer-text)"/><path d="M2 3h6v4H2z M2 3l3 2.3L8 3" fill="none" stroke="var(--footer)" stroke-width="0.8"/></svg>info@risingpaths.com</div>
  <div class="abs f-contact" style="top:1096px"><svg width="7" height="8" viewBox="0 0 10 12"><path d="M5 0a4 4 0 0 1 4 4c0 3-4 8-4 8S1 7 1 4a4 4 0 0 1 4-4z" fill="var(--footer-text)"/><circle cx="5" cy="4" r="1.5" fill="var(--footer)"/></svg>2417 Alder Lane, Brookvale, OR</div>

  <h4 class="abs f-head" style="left:213px">USEFULL LINKS</h4>
  <div class="abs f-link" style="top:1005px">Home</div>
  <div class="abs f-link" style="top:1022px">About Us</div>
  <div class="abs f-link current" style="top:1039px">Our Mission</div>
  <div class="abs f-link" style="top:1056px">Contact Us</div>

  <h4 class="abs f-head" style="left:347px">GALLERY</h4>
  <div class="abs tile" style="left:348px;top:1007px"></div>
  <div class="abs tile active" style="left:389px;top:1007px"></div>
  <svg class="abs" style="left:404px;top:1020px" width="8" height="8" viewBox="0 0 10 10" aria-hidden="true"><circle cx="4" cy="4" r="3" fill="none" stroke="#fff" stroke-width="1.6"/><path d="M6.2 6.2 9 9" stroke="#fff" stroke-width="1.8"/></svg>
  <div class="abs tile" style="left:430px;top:1007px"></div>
  <div class="abs tile" style="left:348px;top:1044px"></div>
  <div class="abs tile" style="left:389px;top:1044px"></div>
  <div class="abs tile" style="left:430px;top:1044px"></div>

  <h4 class="abs f-head" style="left:481px">SUBSCRIBE</h4>
  <div class="abs sub-label">Subscribe to the newsletter</div>
  <div class="abs sub-input">Your email here</div>
  <svg class="abs sub-send" width="9" height="9" viewBox="0 0 10 10" aria-hidden="true"><path d="M0 4.5 10 0 6 10 4.6 5.6Z" fill="#fff"/></svg>
  <div class="abs sub-rule"></div>
  <span class="abs social" style="left:481px"></span>
  <span class="abs social active" style="left:507px"></span>
  <span class="abs social" style="left:532px"></span>
  <span class="abs social" style="left:558px"></span>
  <span class="abs social" style="left:584px"></span>

  <div class="abs copyright">© 2022 Copyright Rising Paths &nbsp;|&nbsp; LLC All rights reserved</div>
</footer>

</body>
</html>
```